Maple Hollow Bloom Backdrops Business card

Looking to have a business card design incorporating my logo for my flower wall business.

Industry/Entity Type

Wedding & event planning

Contact Information for Business Card

My business logo, my name - Jill Worthing (owner), my tagline - Your moments, beautifully framed, phone # 401-627-3918, email address - maplehollowbloombackdrops@fernpost.com, my website - maplehollowbloombackdrops.com, Instagram handle- @maplehollowbloombackdrops, FB handle Handle - maplehollowbloombackdrops

Font styles to use
Other font styles liked:
• Sentaina is the font that is used in my logo

Requirements
Must have
• Would like a double sided business card

```html
<!DOCTYPE html>
<html lang="en">
<head>
<meta charset="utf-8">
<title>Maple Hollow Bloom Backdrops – Business Card</title>
<link rel="stylesheet" href="https://fonts.googleapis.com/css2?family=Crimson+Text&family=Mrs+Saint+Delafield&family=Open+Sans&display=swap">
<style>
  :root {
    --page: #ffffff;
    --card-front: #ffffff;
    --card-back: #f6e4ef;
    --ink: #1d1d1f;
    --gold: #d9b85a;
    --petal-soft: #f8dcec;
    --shadow: rgba(0, 0, 0, 0.45);
  }
  * { box-sizing: border-box; margin: 0; padding: 0; }
  html, body { width: 800px; height: 1200px; overflow: hidden; background: var(--page); }
  .canvas { position: relative; width: 800px; height: 1200px; }

  .card {
    position: absolute;
    left: 60px;
    width: 680px;
    height: 386px;
    overflow: hidden;
    box-shadow: 4px 8px 8px var(--shadow);
  }
  .card--front { top: 184px; background: var(--card-front); }
  .card--back { top: 630px; background: var(--card-back); }

  /* Front: brand seal */
  .brand-seal {
    position: absolute;
    left: 51px; top: 76px;
    width: 226px; height: 226px;
    border: 1.5px solid var(--gold);
    border-radius: 50%;
    display: flex; align-items: center; justify-content: center;
    text-align: center;
  }
  .brand-name {
    font-family: "Crimson Text", serif;
    color: var(--ink);
    font-size: 22px;
    line-height: 1.25;
    letter-spacing: 0.5px;
  }

  .bloom {
    position: absolute;
    background: radial-gradient(ellipse at center, var(--petal-soft) 0%, rgba(248, 220, 236, 0) 70%);
  }
  .bloom--top { left: 523px; top: 0; width: 142px; height: 68px; }
  .bloom--bottom { left: 523px; top: 310px; width: 117px; height: 76px; }

  /* Front: owner */
  .owner-name {
    position: absolute;
    left: 388px; top: 60px;
    font-family: "Mrs Saint Delafield", cursive;
    font-size: 40px;
    line-height: 1;
    color: var(--ink);
    white-space: nowrap;
  }
  .owner-role {
    position: absolute;
    left: 390px; top: 114px;
    font-family: "Crimson Text", serif;
    font-size: 15px;
    line-height: 1;
    color: var(--ink);
  }

  .contact-list { position: absolute; left: 362px; top: 156px; list-style: none; }
  .contact-item {
    display: flex; align-items: center; gap: 14px;
    height: 22px;
    font-family: "Crimson Text", serif;
    font-size: 12.5px;
    color: var(--ink);
    white-space: nowrap;
  }
  .contact-icon { width: 15px; height: 15px; flex: none; }
  .contact-rule {
    width: 198px; margin: 6px 0 10px 29px;
    border-top: 1px dotted var(--ink);
  }
  .social-dot { width: 13px; height: 13px; margin: 0 1px; border-radius: 50%; background: var(--ink); flex: none; }
  .contact-item--social { height: 25px; }

  /* Back */
  .back-brand {
    position: absolute;
    left: 0; right: 0; top: 140px;
    text-align: center;
    font-family: "Crimson Text", serif;
    font-size: 34px;
    color: var(--ink);
    letter-spacing: 0.5px;
  }
  .tagline {
    position: absolute;
    left: 0; right: 0; top: 276px;
    text-align: center;
    font-family: "Open Sans", sans-serif;
    font-size: 17px;
    color: var(--ink);
  }
</style>
</head>
<body>
<main class="canvas">

  <section class="card card--front" aria-label="Business card front">
    <div class="brand-seal">
      <p class="brand-name">Maple Hollow<br>Bloom Backdrops</p>
    </div>

    <div class="bloom bloom--top" role="img" aria-label="Pink line-drawn peony illustration"></div>
    <div class="bloom bloom--bottom" role="img" aria-label="Pink line-drawn peony illustration"></div>

    <p class="owner-name">Jill Worthing</p>
    <p class="owner-role">owner</p>

    <ul class="contact-list">
      <li class="contact-item">
        <svg class="contact-icon" viewBox="0 0 24 24" aria-hidden="true"><path fill="#1d1d1f" d="M6.6 10.8a15.2 15.2 0 0 0 6.6 6.6l2.2-2.2c.3-.3.7-.4 1-.2 1.1.4 2.3.6 3.6.6.6 0 1 .4 1 1V20c0 .6-.4 1-1 1A17 17 0 0 1 3 4c0-.6.4-1 1-1h3.5c.6 0 1 .4 1 1 0 1.3.2 2.5.6 3.6.1.3 0 .7-.2 1z"/></svg>
        <span>401-627-3918</span>
      </li>
      <li class="contact-item">
        <svg class="contact-icon" viewBox="0 0 24 24" aria-hidden="true"><rect x="2" y="5" width="20" height="14" fill="#1d1d1f"/><path d="M2 5l10 8 10-8M2 19l7-7M22 19l-7-7" stroke="#fff" stroke-width="1.5" fill="none"/></svg>
        <span>maplehollowbloombackdrops@fernpost.com</span>
      </li>
      <li class="contact-item">
        <svg class="contact-icon" viewBox="0 0 24 24" aria-hidden="true"><g fill="none" stroke="#1d1d1f" stroke-width="2"><circle cx="12" cy="12" r="9.5"/><ellipse cx="12" cy="12" rx="4" ry="9.5"/><path d="M2.5 12h19M4 7h16M4 17h16"/></g></svg>
        <span>maplehollowbloombackdrops.com</span>
      </li>
      <li class="contact-rule" aria-hidden="true"></li>
      <li class="contact-item contact-item--social">
        <span class="social-dot" aria-hidden="true"></span>
        <span>@maplehollowbloombackdrops</span>
      </li>
      <li class="contact-item contact-item--social">
        <span class="social-dot" aria-hidden="true"></span>
        <span>maplehollowbloombackdrops</span>
      </li>
    </ul>
  </section>

  <section class="card card--back" aria-label="Business card back">
    <p class="back-brand">Maple Hollow Bloom Backdrops</p>
    <p class="tagline">Your moments, beautifully framed</p>
  </section>

</main>
</body>
</html>
```